Ferncrest Dental, LLC business card project

Business card to be designed with current logo.
Dental office- please keep design of card that looks clean and professional.
Please include the following info:
Ferncrest Dental, LLC
Dr. Lorna Pettigrew
2871 Marlowe Street
Bethlehem, PA 18093
610-555-0193
ferncrestdental.office@examplemail.test
Hello everyone-
Reason: Just got back from overseas- will look at all designs and provide feedback. Thank you!
Reason: Polling my friends for the final selection-
thank you to all those that participated- so many talented designers!

```html
<!DOCTYPE html>
<html lang="en">
<head>
<meta charset="utf-8">
<title>Ferncrest Dental, LLC — Business Card</title>
<link rel="stylesheet" href="https://fonts.googleapis.com/css2?family=Raleway:wght@300;400&display=swap">
<style>
  :root {
    --leaf: #a9cf36;
    --leaf-soft: #cfe48f;
    --leaf-deep: #5f9e2c;
    --leaf-text: #7fb52f;
    --paper: #ffffff;
    --backdrop: #f1f2ee;
    --ink-watermark: rgba(255, 255, 255, 0.22);
    --ink-watermark-band: rgba(169, 207, 54, 0.12);
  }
  * { box-sizing: border-box; margin: 0; padding: 0; }
  html, body {
    width: 1200px;
    height: 759px;
    overflow: hidden;
  }
  body {
    background: var(--backdrop);
    font-family: "Raleway", "Helvetica Neue", Arial, sans-serif;
    display: flex;
    align-items: center;
    justify-content: center;
    gap: 60px;
  }
  .card {
    position: relative;
    width: 520px;
    height: 297px;
    overflow: hidden;
    box-shadow: 0 6px 22px rgba(0, 0, 0, 0.12);
  }

  /* Front */
  .card--front {
    background: var(--leaf);
    display: flex;
    align-items: center;
    justify-content: center;
  }
  .brand-name {
    font-weight: 300;
    font-size: 34px;
    letter-spacing: -0.5px;
    color: var(--paper);
    white-space: nowrap;
  }
  .brand-name .brand-suffix { font-size: 34px; }

  /* Back */
  .card--back { background: var(--paper); }
  .back-band {
    position: absolute;
    left: 0; top: 0;
    width: 100%;
    height: 72px;
    background: var(--leaf);
  }
  .back-band-rule {
    position: absolute;
    left: 0; top: 78px;
    width: 100%;
    height: 1px;
    background: var(--leaf-soft);
  }
  .band-watermark {
    position: absolute;
    top: 44px;
    right: 18px;
    font-weight: 300;
    font-size: 44px;
    color: var(--ink-watermark);
    white-space: nowrap;
    line-height: 1;
  }
  .band-watermark--lower {
    top: 80px;
    right: 18px;
    color: var(--ink-watermark-band);
    height: 28px;
    overflow: hidden;
    line-height: 0;
  }
  .contact {
    position: absolute;
    left: 246px;
    top: 116px;
    width: 250px;
  }
  .contact-name {
    font-weight: 400;
    font-size: 19px;
    letter-spacing: 0.4px;
    text-transform: uppercase;
    color: var(--leaf-deep);
    white-space: nowrap;
  }
  .contact-rule {
    margin: 8px 0 10px;
    width: 100%;
    height: 1px;
    background: var(--leaf-soft);
  }
  .contact-list { list-style: none; }
  .contact-item {
    display: flex;
    align-items: center;
    gap: 8px;
    margin-bottom: 7px;
    font-size: 10.5px;
    font-weight: 400;
    color: var(--leaf-text);
    white-space: nowrap;
  }
  .contact-icon {
    width: 11px;
    height: 11px;
    flex: none;
    fill: var(--leaf-deep);
  }
  .back-brand {
    position: absolute;
    left: 26px;
    bottom: 28px;
    font-weight: 300;
    font-size: 20px;
    color: var(--leaf-text);
    white-space: nowrap;
  }
</style>
</head>
<body>

  <section class="card card--front" aria-label="Card front">
    <p class="brand-name">Ferncrest Dental<span class="brand-suffix">, LLC</span></p>
  </section>

  <section class="card card--back" aria-label="Card back">
    <div class="back-band"></div>
    <div class="back-band-rule"></div>
    <span class="band-watermark" aria-hidden="true">Ferncrest Dental</span>

    <div class="contact">
      <h1 class="contact-name">Dr. Lorna Pettigrew</h1>
      <div class="contact-rule"></div>
      <ul class="contact-list">
        <li class="contact-item">
          <svg class="contact-icon" viewBox="0 0 24 24" aria-hidden="true"><path d="M6.6 10.8a15.1 15.1 0 0 0 6.6 6.6l2.2-2.2c.3-.3.7-.4 1-.2 1.1.4 2.3.6 3.6.6.6 0 1 .4 1 1V20c0 .6-.4 1-1 1A17 17 0 0 1 3 4c0-.6.4-1 1-1h3.5c.6 0 1 .4 1 1 0 1.3.2 2.5.6 3.6.1.3 0 .7-.2 1z"/></svg>
          <span>610-555-0193</span>
        </li>
        <li class="contact-item">
          <svg class="contact-icon" viewBox="0 0 24 24" aria-hidden="true"><path d="M2 5h20v14H2zM4 7v.5l8 5 8-5V7l-8 5z"/></svg>
          <span>ferncrestdental.office@examplemail.test</span>
        </li>
        <li class="contact-item">
          <svg class="contact-icon" viewBox="0 0 24 24" aria-hidden="true"><path d="M12 2a7 7 0 0 0-7 7c0 5.2 7 13 7 13s7-7.8 7-13a7 7 0 0 0-7-7zm0 9.5a2.5 2.5 0 1 1 0-5 2.5 2.5 0 0 1 0 5z"/></svg>
          <span>2871 Marlowe Street, Bethlehem, PA 18093</span>
        </li>
      </ul>
    </div>

    <p class="back-brand">Ferncrest Dental, LLC</p>
  </section>

</body>
</html>
```